Car rental website design for a UAE car rental company

This project is about creating a new website design for a car rental company located in Dubai (United Arab Emirates), I opened the same project a few months ago but I didn't receive a lot of appealing entries so I closed it but this time I am marking the project as guaranteed to avoid such situation again, if you have already provided a design before then please re-submit again on this project so that it is considered while reviewing all the designs

A few important things:

1- We need a simple non-complex design
2- The final deliverable would be 2 screens (PSD, JPEG ... etc), the first screen is for the home page and the second screen is for an internal page
3- The home page must have a section that end users can use to rent a car online directly from the home page instead of going into some inner pages
4- The current website is very old and not very appealing so avoid creating a similar design (www.quarvin-drive.example)
5- The name is Quarvin but the company rents normal cars (no Limousin cars will be rented) so avoid adding any fancy cars in the images/graphics used in the design, just normal end users cars
6- The expected pages would be: home, About us, Our team, Strategy, Contact us and links to social media pages
7- The attachments include the company's logo and some screens from other car rental companies that provide online rentals/payments

If you have any questions please feel free to ask and please note that we will need the designs urgently

Thanks

Target Market(s)

Dubai - United Arab Emirates

Industry/Entity Type

It Company

Number of Pages Required

2 page

Font styles to use
Sans Serif

Requirements
Must have
• Check the project details
Nice to have
Should not have

```html
<!DOCTYPE html>
<html lang="en">
<head>
<meta charset="utf-8">
<title>Quarvin Rent A Car</title>
<link href="https://fonts.googleapis.com/css2?family=Open+Sans:wght@400;600;700&family=Russo+One&display=swap" rel="stylesheet">
<style>
:root{
  --orange:#f15a24;
  --ink:#333333;
  --muted:#555555;
  --white:#ffffff;
  --footer:#3a3a3a;
  --page:#ffffff;
  --brand:#a3123a;
}
*{box-sizing:border-box;margin:0;padding:0}
html,body{width:1050px;height:1200px;overflow:hidden;background:var(--page);font-family:"Open Sans",Arial,sans-serif}
.canvas{position:relative;width:1050px;height:1200px;overflow:hidden}

.hero{position:absolute;left:0;top:0;width:1050px;height:340px;
  background:linear-gradient(180deg,#e9eef3 0%,#d9dde0 35%,#c8b9a2 65%,#8aa8a8 85%,#b7a78c 100%)}
.brand-tile{position:absolute;background:var(--white);border-radius:12px;display:flex;align-items:center;justify-content:center;gap:6px}
.brand-tile .mark{width:12px;height:12px;background:var(--brand)}
.brand-tile .name{font-family:"Open Sans",Arial,sans-serif;font-weight:700;color:var(--brand)}
.hero .brand-tile{left:472px;top:96px;width:116px;height:104px}
.hero .brand-tile .name{font-size:20px}
.hero-title{position:absolute;left:0;top:218px;width:1050px;text-align:center;font-family:"Russo One",Arial,sans-serif;
  color:var(--white);font-size:21px;line-height:24px;letter-spacing:1px;text-shadow:0 1px 3px rgba(0,0,0,.45)}

.column{position:absolute;left:259px;top:340px;width:527px;height:783px;background:var(--white);box-shadow:0 0 8px rgba(0,0,0,.35)}
.nav{position:absolute;left:0;top:0;width:527px;height:32px;background:var(--orange);display:flex;justify-content:space-between;align-items:center;padding:0 28px 0 38px}
.nav a{color:var(--white);text-decoration:none;font-size:9px}

.slider{position:absolute;left:0;top:32px;width:527px;height:220px;
  background:radial-gradient(ellipse at 50% 55%,#3a3a3a 0%,#1e1e1e 35%,#6b5a4c 70%,#9a8a7a 100%)}
.slider-arrow{position:absolute;top:98px;width:15px;height:22px;background:var(--white);color:#777;font-size:10px;line-height:22px;text-align:center}
.slider-arrow.prev{left:0}
.slider-arrow.next{right:0}
.book-car{position:absolute;left:214px;top:236px;width:115px;height:32px;background:var(--orange);color:var(--white);font-size:10px;line-height:32px;text-align:center}

.about{position:absolute;left:0;top:252px;width:527px;height:202px}
.about .brand-tile{left:21px;top:58px;width:90px;height:75px;border-radius:0}
.about .brand-tile .name{font-size:16px}
.about-text{position:absolute;left:130px;top:76px;width:360px;font-size:7.5px;line-height:10px;color:var(--ink)}
.about-text .lead{color:var(--orange)}
.about-text p{text-indent:16px}

.booking{position:absolute;left:0;top:454px;width:527px;height:329px;
  background:radial-gradient(ellipse at 40% 55%,#5a6670 0%,#1f252b 45%,#0d1014 75%,#3a2418 100%)}
.booking-title{position:absolute;left:24px;top:102px;font-family:"Russo One",Arial,sans-serif;color:var(--white);font-size:27px;line-height:41px;letter-spacing:1px}
.form{position:absolute;left:306px;top:32px;width:120px;height:280px}
.form label{display:block;text-align:center;color:var(--white);font-size:7.5px;height:13px;line-height:13px}
.form .field{height:17px;border-radius:8px;background:var(--white);color:#aaa;font-size:7px;line-height:17px;text-align:center}
.form .row{height:30.5px}
.form .field.message{height:42px;border-radius:9px;line-height:12px;padding-top:3px}
.form .submit{position:absolute;left:27px;top:254px;width:72px;height:16px;background:var(--orange);color:var(--white);font-size:7.5px;line-height:16px;text-align:center}

.footer{position:absolute;left:0;top:1123px;width:1050px;height:77px;background:var(--footer)}
.footer .brand-tile{left:259px;top:14px;width:57px;height:51px;border-radius:8px;gap:3px}
.footer .brand-tile .mark{width:7px;height:7px}
.footer .brand-tile .name{font-size:10px}
.footer-nav{position:absolute;left:376px;top:30px;display:flex}
.footer-nav a{color:var(--white);text-decoration:none;font-size:7.5px;margin-right:32px}
.copyright{position:absolute;left:0;top:58px;width:1050px;text-align:center;color:#ddd;font-size:7px}
</style>
</head>
<body>
<div class="canvas">
  <header class="hero" role="img" aria-label="Aerial photograph of the Dubai skyline with a tall tower and waterways">
    <div class="brand-tile"><span class="mark"></span><span class="name">Quarvin</span></div>
    <h1 class="hero-title">Welcome to Quarvin<br>The Best of Dubai</h1>
  </header>

  <main class="column">
    <nav class="nav">
      <a href="#">Home</a><a href="#">Book Now</a><a href="#">About Us</a><a href="#">Our Team</a><a href="#">Strategy</a>
    </nav>

    <section class="slider" role="img" aria-label="Photograph of a black sedan parked in a warehouse">
      <div class="slider-arrow prev">&lsaquo;</div>
      <div class="slider-arrow next">&rsaquo;</div>
    </section>
    <div class="book-car">Book this Car now</div>

    <section class="about">
      <div class="brand-tile"><span class="mark"></span><span class="name">Quarvin</span></div>
      <div class="about-text">
        <p class="lead">As Dubai is expected to welcome millions of tourists and visitors, car rental industry is believed to escalate more rapidly in the region.</p>
        <p>Over the past five years, demands for car rentals in Dubai has been augmenting at a healthy pace and is currently registering a growth rate of 20 to 25 percent per year. The swift economic growth and the number...</p>
      </div>
    </section>

    <section class="booking" role="img" aria-label="Close-up photograph of car keys in an ignition">
      <h2 class="booking-title">Book Now<br>for a Ride</h2>
      <form class="form">
        <div class="row"><label>Name:</label><div class="field">Enter Name</div></div>
        <div class="row"><label>Email:</label><div class="field">Enter Email</div></div>
        <div class="row"><label>Company:</label><div class="field">Enter Company</div></div>
        <div class="row"><label>Work Address:</label><div class="field">Enter Address</div></div>
        <div class="row"><label>City:</label><div class="field">Enter City</div></div>
        <div class="row"><label>Country:</label><div class="field">Enter Country</div></div>
        <div class="row"><label>Message:</label><div class="field message">Enter Your Message</div></div>
        <div class="submit">Book Now</div>
      </form>
    </section>
  </main>

  <footer class="footer">
    <div class="brand-tile"><span class="mark"></span><span class="name">Quarvin</span></div>
    <nav class="footer-nav">
      <a href="#">Home</a><a href="#">About us</a><a href="#">Book Now</a><a href="#">Our Team</a><a href="#">Strategy</a>
    </nav>
    <p class="copyright">&copy;Copyright 2015, Quarvin. All rights reserved.</p>
  </footer>
</div>
</body>
</html>
```